Colin Vesk Personal Card

I am looking for a personal card that has my contact information on the front and then the url for my website on the back. I am a fan of minimal, modern design, but am very open minded to other styles. Both portrait and landscape designs are acceptable. The only other specification that I have is that some sort of graphic of a raven is present somewhere on the card (my last name 'Vesk' means raven in German).
Industry/Entity Type
Landscape
Contact Information for Business Card
Colin Vesk
508.641.2093
colintvesk@postvale.com
colintvesk.com
Colors
Designer to choose colors to be used in the design.
Requirements
Must have
- Raven on some part of the card

```html
<!DOCTYPE html>
<html lang="en">
<head>
<meta charset="utf-8">
<title>Colin Vesk Personal Card</title>
<link href="https://fonts.googleapis.com/css2?family=Open+Sans:wght@400&family=Poppins:wght@600&family=Questrial&display=swap" rel="stylesheet">
<style>
  :root {
    --backdrop: #6e5538;
    --card-dark: #07080a;
    --card-dark-glow: #262626;
    --card-light: #ffffff;
    --ink: #1e1e1e;
    --ink-light: #ffffff;
    --raven-grey: rgba(190, 190, 192, 0.78);
  }
  * { margin: 0; padding: 0; box-sizing: border-box; }
  html, body {
    width: 1200px;
    height: 1000px;
    overflow: hidden;
    background: var(--backdrop);
  }
  .canvas {
    position: relative;
    width: 1200px;
    height: 1000px;
  }
  .card {
    position: absolute;
    top: 182px;
    width: 398px;
    height: 666px;
    border-radius: 30px;
    overflow: hidden;
  }
  .card--back {
    left: 170px;
    background: radial-gradient(circle at 55% 48%, var(--card-dark-glow) 0%, var(--card-dark) 62%);
  }
  .card--front {
    left: 567px;
    background: var(--card-light);
  }
  .website {
    position: absolute;
    left: 0;
    right: 0;
    bottom: 28px;
    text-align: center;
    font-family: "Open Sans", sans-serif;
    font-size: 22px;
    color: var(--ink-light);
  }
  .raven-artwork {
    position: absolute;
    left: 240px;
    top: 225px;
    width: 595px;
    height: 445px;
    border-radius: 48% 52% 46% 54% / 50% 44% 56% 50%;
    background: radial-gradient(ellipse at 55% 50%, var(--raven-grey) 0%, rgba(190,190,192,0.5) 70%, rgba(190,190,192,0) 100%);
  }
  .contact {
    position: absolute;
    right: 30px;
    bottom: 34px;
    text-align: right;
    color: var(--ink);
  }
  .contact__name {
    font-family: "Poppins", sans-serif;
    font-weight: 600;
    font-size: 28px;
    margin-bottom: 34px;
    margin-right: 4px;
  }
  .contact__line {
    display: flex;
    justify-content: flex-end;
    align-items: center;
    gap: 7px;
    font-family: "Questrial", sans-serif;
    font-size: 18px;
    line-height: 26px;
  }
  .contact__icon {
    width: 19px;
    height: 19px;
  }
</style>
</head>
<body>
<div class="canvas">
  <section class="card card--back">
    <p class="website">colintvesk.com</p>
  </section>

  <section class="card card--front">
    <div class="contact">
      <h1 class="contact__name">Colin Vesk</h1>
      <p class="contact__line">508.641.2093
        <svg class="contact__icon" viewBox="0 0 20 20" aria-hidden="true">
          <circle cx="10" cy="10" r="9" fill="#1e1e1e"/>
          <circle cx="10" cy="10" r="7.4" fill="#fff"/>
          <rect x="6.5" y="4.5" width="7" height="11" rx="1.3" fill="#1e1e1e"/>
          <rect x="7.8" y="6" width="4.4" height="5.5" fill="#fff"/>
        </svg>
      </p>
      <p class="contact__line">colintvesk@postvale.com
        <svg class="contact__icon" viewBox="0 0 20 20" aria-hidden="true">
          <circle cx="10" cy="10" r="9" fill="#1e1e1e"/>
          <circle cx="10" cy="10" r="7.4" fill="#fff"/>
          <rect x="5" y="6.5" width="10" height="7" rx="1" fill="#1e1e1e"/>
          <path d="M5.6 7.2 L10 10.6 L14.4 7.2" fill="none" stroke="#fff" stroke-width="1.1"/>
        </svg>
      </p>
    </div>
  </section>

  <div class="raven-artwork" role="img" aria-label="Grey silhouette of a raven in flight spanning both sides of the card"></div>
</div>
</body>
</html>
```